Web site for Life Coaching Consultant

I require a website for a life coaching business. I have a Tidal Netware account which I set up last week. I will need to be able to add articles and testimonials. The design should communicate that RL Harbor Lanterns is there to help people breakdown personal barriers and that we are an advocate to help them achieve personal goals.
Updates

Reason: I have some designers just accepting my invitation to submit so to give them a few days to submit. I have been thrilled with the quality of the submissions Thank you.

Hi everyone

I am loving all your designs.  The only feedback I can get from people is that they feel that the runner makes the web page look like a personal coach rather than a life coach that helps people with relations, career, and personal road blocks.

Sorry                                   

Reason: Hi I have increased the deadline as there has been so many amazing designs and some of you have asked to fine tune your entries. I would like to take this opportunity to thank you all. It is going to be a tough decision. I have put a few more pictures on the project page hoping this will help

Hi I just wanted to thank you all for your great designs.  As I got so many good designs I have asked people to vote.  I will be in touch in the next day or 2.

Cheers

Target Market(s)

People with self esteem issues either woman or girls, people who want to goal set and need an advocate

Industry/Entity Type

Life Coaching

Colors
d2a4cc
e567a6

Requirements
Must have
• must have bio section, logo, articles page, affirmation section and testimonial page.

```html
<!DOCTYPE html>
<html lang="en">
<head>
<meta charset="utf-8">
<title>RL Harbor Lanterns – Life Coaching</title>
<link href="https://fonts.googleapis.com/css2?family=Source+Sans+3:wght@400;600;700&family=Arimo:wght@400;700&display=swap" rel="stylesheet">
<style>
:root{
  --pink:#e2176f;
  --pink-soft:#e567a6;
  --ink:#333;
  --muted:#666;
  --blue:#2f8fd8;
  --band:#f2f2f2;
  --footer:#2e2e2e;
  --footer-bottom:#262626;
  --white:#fff;
}
*{margin:0;padding:0;box-sizing:border-box}
html,body{width:754px;height:1200px;overflow:hidden;background:var(--white)}
body{position:relative;font-family:"Arimo",Arial,sans-serif;color:var(--ink)}
.abs{position:absolute}
.head-font{font-family:"Source Sans 3",sans-serif}

/* header */
.brand{left:54px;top:26px;display:flex;align-items:center;gap:8px}
.brand-dot{width:22px;height:22px;border-radius:50%;background:var(--pink)}
.brand-name{font-family:"Source Sans 3",sans-serif;font-weight:700;font-size:17px;color:var(--pink);line-height:1.05;width:90px}
.phone{right:56px;top:19px;font-size:11px;color:#444;display:flex;align-items:center;gap:6px}
.nav{top:50px;left:324px;display:flex;font-size:10.5px;color:#555}
.nav a{color:inherit;text-decoration:none;height:23px;line-height:23px}
.nav .active{background:var(--pink);color:var(--white);padding:0 10px}

/* hero */
.hero{left:0;top:87px;width:754px;height:255px;background:linear-gradient(100deg,#1c4f64 0%,#3f86a6 35%,#8bbcd0 65%,#e8e2d2 100%)}
.hero-figure{left:470px;top:115px;width:100px;height:205px;background:linear-gradient(#2a2a2a,#1a1a1a);border-radius:40px 40px 8px 8px;opacity:.85}
.hero-title{left:170px;top:147px;color:var(--white);font-family:"Source Sans 3",sans-serif;font-weight:700;line-height:1}
.hero-title .l1{font-size:29px;display:block}
.hero-title .l2{font-size:21px;display:block;margin-top:5px}
.hero-text{left:170px;top:216px;width:210px;font-size:8.5px;line-height:16px;color:#eef}
.arrow{top:199px;width:30px;height:30px;border-radius:50%;background:rgba(80,80,80,.7)}

/* sections */
.section-title{font-family:"Source Sans 3",sans-serif;color:var(--pink);font-size:15px;font-weight:400}
.photo{background:linear-gradient(#3b3552,#d98a3c 60%,#2a2224)}
.welcome-text{left:226px;top:395px;width:475px;font-size:8.6px;line-height:14.4px;color:#555;text-align:justify}

.thumb{width:84px;height:77px;border:1px solid #ddd;padding:3px;background:var(--white)}
.thumb div{width:100%;height:100%}
.article-title{font-family:"Source Sans 3",sans-serif;font-size:11.5px;color:#333;font-weight:400}
.article-text{width:310px;font-family:"Source Sans 3",sans-serif;font-size:8px;line-height:13.5px;color:#444}
.meta{font-family:"Source Sans 3",sans-serif;font-size:7px;font-style:italic;color:#555;display:flex;align-items:center;gap:12px}
.chip{font-style:normal;font-size:7.5px;padding:2px 6px;border:1px solid #c9d6e6;background:#eef3f9;color:#3a5a8a;border-radius:2px}
.about-frame{left:490px;top:574px;width:208px;height:96px;border:1px solid #ccc;padding:4px}
.about-text{left:490px;top:682px;width:210px;font-family:"Source Sans 3",sans-serif;font-size:8px;line-height:13.5px;color:#444}

/* testimonials */
.band{left:0;top:782px;width:754px;height:196px;background:var(--band)}
.avatar{width:90px;height:90px;border-radius:50%;border:4px solid var(--white);box-shadow:0 0 0 1px #ddd;background:linear-gradient(#dfe6ea,#c9d3d9)}
.quote{width:180px;font-size:8.6px;line-height:15px;color:#666}
.quote-name{font-size:8.6px;color:var(--blue);text-align:right;margin-top:4px}

/* footer */
.footer{left:0;top:978px;width:754px;height:168px;background:var(--footer)}
.footer-bottom{left:0;top:1146px;width:754px;height:54px;background:var(--footer-bottom);border-top:1px solid #3a3a3a}
.f-head{color:var(--white);font-size:10px;font-weight:700;top:1006px}
.f-links{top:1028px;list-style:none;font-family:"Source Sans 3",sans-serif;font-size:9.5px;color:#ddd;line-height:18px}
.social{top:1032px;width:22px;height:22px}
.news-text{left:531px;top:1028px;width:175px;font-family:"Source Sans 3",sans-serif;font-size:9.5px;line-height:18px;color:var(--white)}
.news-input{left:531px;top:1070px;width:170px;height:22px;background:var(--white);border:none}
.subscribe{left:624px;top:1103px;width:76px;height:23px;background:var(--blue);color:var(--white);font-family:"Source Sans 3",sans-serif;font-size:10.5px;text-align:center;line-height:23px}
.copy{left:55px;top:1161px;font-size:8.6px;color:#ddd}
</style>
</head>
<body>

<header>
  <div class="abs brand"><span class="brand-dot"></span><span class="brand-name">RL Harbor Lanterns</span></div>
  <div class="abs phone">
    <svg width="10" height="12" viewBox="0 0 10 12"><path d="M7 1 C3 2 2 6 3 11 L5 10 C4 7 4 5 7 3 Z" fill="#555"/></svg>
    903-555-0142
  </div>
  <nav class="abs nav">
    <a class="active" href="#">Home</a>
    <a href="#" style="margin-left:22px">About Us</a>
    <a href="#" style="margin-left:32px">Latest Articles</a>
    <a href="#" style="margin-left:33px">Testimonials</a>
    <a href="#" style="margin-left:32px">Contact</a>
  </nav>
</header>

<section class="abs hero" role="img" aria-label="Woman standing confidently against a bright cloudy sky"></section>
<div class="abs hero-figure" role="img" aria-label="Silhouette of a woman standing tall"></div>
<h1 class="abs hero-title"><span class="l1">I AM STRONGER</span><span class="l2">THAN ANY EXCUSE.</span></h1>
<p class="abs hero-text">Duis autem vel eum iriure dolor in hendrerit in vulputate velit esse molestie consequat, vel illum dolore eu feugiat nulla facilisis at vero.</p>
<div class="abs arrow" style="left:54px"><svg width="30" height="30"><path d="M17 9 L11 15 L17 21" stroke="#fff" stroke-width="2" fill="none"/></svg></div>
<div class="abs arrow" style="left:668px"><svg width="30" height="30"><path d="M13 9 L19 15 L13 21" stroke="#fff" stroke-width="2" fill="none"/></svg></div>

<h2 class="abs section-title" style="left:54px;top:359px">Welcome to RL Harbor Lanterns</h2>
<div class="abs photo" style="left:54px;top:396px;width:154px;height:98px" role="img" aria-label="Person with raised arms on a hilltop at sunset"></div>
<p class="abs welcome-text">Typi non habent claritatem insitam; est usius legentis in iis qui facit eorum claritatem. Invenistigationes demonstraverunt ectores legere me lius quod ii legunt saepius. Claritas est etiam processus dynamicus, qui sequitur mutationem consuet udium lectorum. Mirum est notare quam littera gothica Duis autem vel eum iriure dolor in hendrerit in vulputate velit ess e molestie consequat, vel illum dolore eiu feugiat nulla facilisis at vero eros et accumsan et iusto odio dignissim qui blan dit praesent luptatum zzril delenit augue duis dolore te feugait nulla facilisi. Nam liber temiipor cum soluta nobis eleifend option congue nihil imperdiet doming id quod mazim placerat facer possim assum. Typi non habent claritatem insitam; e st usus legentis in iis qui facit</p>

<h2 class="abs section-title" style="left:54px;top:533px">Latest Articles</h2>
<h2 class="abs section-title" style="left:490px;top:533px">About Us</h2>

<article>
  <div class="abs thumb" style="left:54px;top:573px"><div class="photo" role="img" aria-label="Two people celebrating on a rock at sunset"></div></div>
  <h3 class="abs article-title" style="left:151px;top:571px">Suspendisse eu erat quam. Vivamus porttitor eros quis.</h3>
  <p class="abs article-text" style="left:151px;top:589px">Suspendisse eu erat quam. Vivamus porttitor eros quis nisi lacinia sed interdum uam a orci quis nisi sagittis sagittis. Etiam adipiscing, justo quis feugiat.Suspend amus porttitor eros quis nisi lacinia sed interdum lorem vulputate.</p>
  <div class="abs meta" style="left:151px;top:634px">Posted on 02 June, 2013 <span class="chip">Follow</span><span class="chip">Like</span></div>
</article>
<article>
  <div class="abs thumb" style="left:54px;top:665px"><div style="background:linear-gradient(#5f8a3a,#a7c46a)" role="img" aria-label="Woman with open arms in a sunny green field"></div></div>
  <h3 class="abs article-title" style="left:151px;top:662px">Suspendisse eu erat quam. Vivamus porttitor eros quis.</h3>
  <p class="abs article-text" style="left:151px;top:680px">Suspendisse eu erat quam. Vivamus porttitor eros quis nisi lacinia sed interdum uam a orci quis nisi sagittis sagittis. Etiam adipiscing, justo quis feugiat.Suspend amus porttitor eros quis nisi lacinia sed interdum lorem vulputate.</p>
  <div class="abs meta" style="left:151px;top:726px">Posted on 02 June, 2013 <span class="chip">Follow</span><span class="chip">Like</span></div>
</article>

<div class="abs about-frame"><div style="width:100%;height:100%;background:linear-gradient(#2f6fc4,#7aaee6)" role="img" aria-label="Three friends jumping joyfully against a blue sky"></div></div>
<p class="abs about-text">Typi non habent claritatem insitam; est usus legentisinii s qui facit eorum claritatem. Investigationes demonstav erunt lectores legere melius quod ii legunt saepius. Clar itas est etiam processus dynamicus, qui sequitur.</p>

<section class="abs band"></section>
<h2 class="abs section-title" style="left:0;width:754px;text-align:center;top:801px;font-size:17px">Testimonials</h2>
<div class="abs avatar" style="left:61px;top:841px" role="img" aria-label="Portrait of a smiling client"></div>
<div class="abs" style="left:174px;top:849px">
  <p class="quote">Quisa. Vestibulum libiero nisl, porta vel, scel erisque eget, malesa. Nam liber tempor cum soluta nobis eleifend option congue nihil imp erdiet doming id quod mazim placerat. Clarit as est etiam processus dynamicus.</p>
  <p class="quote-name">- Nora Castell</p>
</div>
<div class="abs avatar" style="left:408px;top:841px" role="img" aria-label="Portrait of a smiling client"></div>
<div class="abs" style="left:520px;top:849px">
  <p class="quote">Quisa. Vestibulum libiero nisl, porta vel, scel erisque eget, malesa. Nam liber tempor cum soluta nobis eleifend option congue nihil imp erdiet doming id quod mazim placerat. Clarit as est etiam processus dynamicus.</p>
  <p class="quote-name" style="width:175px">- Idris Walden</p>
</div>

<footer>
  <div class="abs footer"></div>
  <h4 class="abs f-head" style="left:55px">Quick Links</h4>
  <ul class="abs f-links" style="left:55px"><li>Home</li><li>About</li><li>Services</li><li>Blog</li><li>Testimonials</li></ul>
  <h4 class="abs f-head" style="left:208px">About</h4>
  <ul class="abs f-links" style="left:209px"><li>About us</li><li>Contact Us</li><li>Help</li><li>Privacy Policy</li><li>Terms Of Service</li></ul>
  <h4 class="abs f-head" style="left:351px">Follow us on</h4>
  <div class="abs social" style="left:351px;background:#3b5fa8"></div>
  <div class="abs social" style="left:381px;background:#2b9bd8"></div>
  <div class="abs social" style="left:412px;background:#f26a22"></div>
  <div class="abs social" style="left:443px;background:#e0262c"></div>
  <h4 class="abs f-head" style="left:531px">Newsletter</h4>
  <p class="abs news-text">Stay in touch with us by signing up for our quarterly newsletter!</p>
  <div class="abs news-input"></div>
  <div class="abs subscribe">SUBSCRIBE</div>
  <div class="abs footer-bottom"></div>
  <p class="abs copy">Copyright ©2013. All Rights Reserved.</p>
</footer>

</body>
</html>
```